Esthetically Pleasing Core Values and Brand Promise for Accounting Firm

I would like a cohesive design that ties together my core values and brand promise. My firm, Maple Finch Advisory, provides accounting work to small businesses. I prefer modern and clean designs. I want my Core Values and Brand Promise to represent me - sole entrepreneur, married, mother of two kids, modern esthetics, clean lines, organized, colorful (teals, greys, white, yellows)

Industry/Entity Type

Public Accounting

Colors
33b8a4

```html
<!DOCTYPE html>
<html lang="en">
<head>
<meta charset="utf-8">
<title>Maple Finch Advisory – Core Values and Brand Promise</title>
<link rel="stylesheet" href="https://fonts.googleapis.com/css2?family=Poppins:wght@700&family=Roboto:wght@400&family=Source+Sans+3:wght@400&display=swap">
<style>
  :root {
    --backdrop: #efefed;
    --teal: #138b84;
    --teal-deep: #0f7f78;
    --yellow: #e3d760;
    --cream: #e4e0b0;
    --ring-1: #e9e4ac;
    --ring-2: #e6de9a;
    --ring-3: #e9d78f;
    --ring-4: #e4da5c;
    --ring-5: #ddd25b;
    --mark: #1a8a7f;
  }
  * { margin: 0; padding: 0; box-sizing: border-box; }
  html, body { width: 1136px; height: 1200px; overflow: hidden; background: var(--backdrop); }
  .poster {
    position: absolute; left: 168px; top: 30px;
    width: 800px; height: 1140px;
    background: var(--teal);
    overflow: hidden;
  }
  .rings { position: absolute; left: 0; top: 0; }
  .section-title {
    position: absolute; left: 54px;
    font-family: "Poppins", sans-serif; font-weight: 700;
    color: var(--yellow); font-size: 48px; line-height: 54px;
    letter-spacing: 0.5px;
  }
  .value { position: absolute; left: 56px; width: 300px; }
  .value-name {
    font-family: "Roboto", sans-serif; font-weight: 400;
    color: var(--cream); font-size: 39px; line-height: 44px;
  }
  .value-text {
    margin-top: 4px;
    font-family: "Source Sans 3", sans-serif;
    color: var(--cream); font-size: 15px; line-height: 20px;
  }
  .promise-list { position: absolute; left: 54px; top: 806px; list-style: none; }
  .promise-list li {
    font-family: "Roboto", sans-serif;
    color: var(--cream); font-size: 42px; line-height: 61px;
  }
  .service {
    position: absolute; top: 1032px; width: 330px;
    font-family: "Source Sans 3", sans-serif;
    color: var(--cream); font-size: 14.5px; line-height: 18px;
  }
  .service--tax { left: 56px; }
  .service--accounting { left: 426px; top: 1034px; }
  .brand-name {
    position: absolute; left: 560px; top: 458px; width: 200px;
    text-align: center;
    font-family: "Roboto", sans-serif; font-weight: 400;
    color: var(--mark); font-size: 30px; line-height: 36px;
    letter-spacing: 2px;
  }
</style>
</head>
<body>
  <main class="poster">
    <svg class="rings" width="800" height="1140" viewBox="0 0 800 1140" aria-hidden="true">
      <circle cx="786" cy="496" r="457" fill="var(--ring-1)"/>
      <circle cx="786" cy="496" r="409" fill="var(--ring-2)"/>
      <circle cx="786" cy="496" r="364" fill="var(--ring-3)"/>
      <circle cx="786" cy="496" r="316" fill="var(--ring-4)"/>
      <circle cx="786" cy="496" r="270" fill="var(--ring-5)"/>
    </svg>

    <h1 class="section-title" style="top:56px">CORE VALUES</h1>

    <div class="value" style="top:136px">
      <h2 class="value-name">empower</h2>
      <p class="value-text">we are dedicated, appreciative and respectful of people's time and purpose.</p>
    </div>
    <div class="value" style="top:248px">
      <h2 class="value-name">client focused</h2>
      <p class="value-text">we provide a personal service that goes above the standards of professional care.</p>
    </div>
    <div class="value" style="top:378px">
      <h2 class="value-name">rectitude</h2>
      <p class="value-text">we know the difference<br>between what we have the<br>right to do and what the right<br>thing to do is.</p>
    </div>
    <div class="value" style="top:529px">
      <h2 class="value-name">relentless</h2>
      <p class="value-text">We believe that the longer<br>we try to do our best, the<br>better we become.</p>
    </div>

    <h1 class="section-title" style="top:688px">BRAND<br>PROMISE</h1>
    <ul class="promise-list">
      <li>trust</li>
      <li>dependability</li>
      <li>transparency</li>
    </ul>

    <p class="service service--tax">Tax - Maple Finch provides all clients with a trusted tax advisor who provides accuracy in all filings and ensures your compliance with all government agencies.</p>
    <p class="service service--accounting">Accounting - Maple Finch provides all business owners with the financial visibility needed to foster growth and facilitate goals.</p>

    <p class="brand-name">MAPLE FINCH<br>ADVISORY</p>
  </main>
</body>
</html>
```